DOG DAYCARE BILLBOARD

Design a bold exciting billboard that can be read easily from a distance! Our goal is brand awareness and showcasing the services we offer (Boarding, Grooming, Daycare, and Training.
we would like to see examples with the phrase "your best friend's best day". Our name Bright Meadow Canine Activity Center (or just Bright Meadow might work better and could be bigger) and the services we provide.
(there are two examples of what we like included in the pictures)
you can find more information o our website at pawplayhub@mailnest.example.

```html
<!DOCTYPE html>
<html lang="en">
<head>
<meta charset="utf-8">
<title>Bright Meadow Billboard</title>
<link rel="stylesheet" href="https://fonts.googleapis.com/css2?family=Montserrat:wght@700;800;900&display=swap">
<style>
  :root {
    --stage: #eef1f3;
    --brand-yellow: #e6c83c;
    --ink-black: #0b0b0b;
    --arrow-gray: #a8a8aa;
    --headline-gray: #3a3a3b;
    --photo-warm: #8a5a2e;
    --photo-cool: #3f5a5c;
  }
  html, body {
    margin: 0;
    width: 1200px;
    height: 801px;
    overflow: hidden;
    background: var(--stage);
  }
  .billboard {
    position: absolute;
    left: 28px;
    top: 136px;
    width: 1145px;
    height: 529px;
    display: block;
  }
  .billboard text {
    font-family: "Montserrat", sans-serif;
    font-weight: 800;
  }
  .tagline-small { fill: var(--headline-gray); font-size: 27px; }
  .tagline-large { fill: var(--headline-gray); font-size: 64px; font-weight: 900; letter-spacing: -1px; }
  .service-name { fill: var(--brand-yellow); font-size: 44px; }
  .service-tick { fill: none; stroke: var(--brand-yellow); }
  .contact-line { fill: var(--ink-black); font-size: 24px; }
  .location-line { fill: var(--ink-black); font-size: 22px; }
  .brand-name { fill: var(--ink-black); font-size: 24px; }
</style>
</head>
<body>
<svg class="billboard" viewBox="0 0 1145 529" xmlns="http://www.w3.org/2000/svg">
  <defs>
    <linearGradient id="photo-tone" x1="0" y1="0" x2="1" y2="1">
      <stop offset="0" stop-color="var(--photo-cool)"/>
      <stop offset="0.45" stop-color="var(--photo-warm)"/>
      <stop offset="1" stop-color="var(--photo-cool)"/>
    </linearGradient>
    <linearGradient id="edge-shadow" x1="0" y1="0" x2="1" y2="0">
      <stop offset="0" stop-color="#000" stop-opacity="0"/>
      <stop offset="1" stop-color="#000" stop-opacity="0.9"/>
    </linearGradient>
  </defs>

  <g class="photo-area" role="img" aria-label="Photo of a happy golden retriever swimming among colourful plastic balls">
    <rect x="0" y="0" width="620" height="529" fill="url(#photo-tone)"/>
  </g>

  <polygon class="edge-shadow" points="530,0 600,0 560,264 600,529 530,529 490,264" fill="url(#edge-shadow)"/>
  <polygon class="yellow-panel" points="597,0 1145,0 1145,529 597,529 557,264" fill="var(--brand-yellow)"/>

  <polygon class="services-panel" points="735,136 1145,136 1145,392 735,392 760,264" fill="var(--ink-black)"/>
  <polygon class="tagline-arrow" points="490,136 737,136 712,264 737,392 490,392 435,264" fill="var(--arrow-gray)"/>
  <polygon class="divider-chevron" points="690,190 740,190 716,264 740,338 690,338 714,264" fill="var(--brand-yellow)"/>

  <text class="tagline-small" x="590" y="192" text-anchor="middle">YOUR BEST</text>
  <text class="tagline-small" x="590" y="222" text-anchor="middle">FRIEND'S</text>
  <text class="tagline-large" x="590" y="294" text-anchor="middle">BEST</text>
  <text class="tagline-large" x="590" y="355" text-anchor="middle">DAY</text>

  <g class="service-list">
    <g class="service-tick" stroke-width="4">
      <rect x="764" y="166" width="34" height="34" rx="4"/>
      <rect x="764" y="218" width="34" height="34" rx="4"/>
      <rect x="764" y="270" width="34" height="34" rx="4"/>
      <rect x="764" y="322" width="34" height="34" rx="4"/>
    </g>
    <g class="service-tick" stroke-width="7" stroke-linecap="round" stroke-linejoin="round">
      <polyline points="771,182 780,193 806,160"/>
      <polyline points="771,234 780,245 806,212"/>
      <polyline points="771,286 780,297 806,264"/>
      <polyline points="771,338 780,349 806,316"/>
    </g>
    <text class="service-name" x="822" y="199">BOARDING</text>
    <text class="service-name" x="822" y="251">DAYCARE</text>
    <text class="service-name" x="822" y="303">GROOMING</text>
    <text class="service-name" x="822" y="355">TRAINING</text>
  </g>

  <g class="brand-mark">
    <circle cx="1000" cy="68" r="30" fill="var(--ink-black)"/>
    <text class="brand-name" x="1092" y="124" text-anchor="end">BRIGHT MEADOW</text>
  </g>

  <text class="contact-line" x="862" y="452" text-anchor="middle">PAWPLAYHUB@MAILNEST.EXAMPLE</text>
  <text class="location-line" x="862" y="487" text-anchor="middle">›››› WILLOW BEND IA ‹‹‹‹</text>
</svg>
</body>
</html>
```